** Wanted ** Wordpress web design for scaffolding rental and construction company

We need a website design and must be functional to show a basic overview of what our company offers as a service. We have a domain name and a logo but we need web design. This web site should have another scaffolding rental page for construction and renovation as well as a quote section where customers can enter their personal information and also upload photos. The site% 26quot; www.brixmorvo.com% 26quot; should be intuitive, clear and classy ... The logo must be found on the site in several ways.

Target Market(s)

Professional and no professional

Coding

Coded - Design and coding required

Number of Pages Required

3 page

Font styles to use
Serif
Sans Serif
Decorative
Script

Requirements
Must have
• Our logo
Nice to have
• Slogan:% 26quot; The height% 26 # 224; port% 26 # 233; e hand% 26quot;

```html
<!DOCTYPE html>
<html lang="en">
<head>
<meta charset="utf-8">
<title>Brixmorvo – Scaffolding, Elevation &amp; Renovation</title>
<link href="https://fonts.googleapis.com/css2?family=Roboto+Condensed:wght@400;700&family=Montserrat:wght@400;500;600&display=swap" rel="stylesheet">
<style>
:root{
  --orange:#f28a1c;
  --dark:#1d1b1a;
  --ink:#111111;
  --body:#6b6b6b;
  --white:#ffffff;
  --dot:#f3a25a;
  --line:rgba(255,255,255,.35);
}
*{margin:0;padding:0;box-sizing:border-box}
html,body{width:1200px;height:4501px;overflow:hidden}
body{position:relative;background:var(--white);font-family:"Montserrat",sans-serif;color:var(--body)}
.abs{position:absolute}
.heading{font-family:"Roboto Condensed",sans-serif;font-weight:700;color:var(--ink)}
.center{left:0;width:1200px;text-align:center}
.small{font-size:10px;line-height:20px}
.btn{position:absolute;background:var(--orange);color:var(--white);font-family:"Roboto Condensed",sans-serif;font-weight:700;display:flex;align-items:center;justify-content:center}
.photo{position:absolute}
.dots{position:absolute;background-image:radial-gradient(circle,var(--dot) 1.6px,transparent 2px);background-size:13px 13px}

/* header + hero */
.hero{position:absolute;left:0;top:0;width:1200px;height:638px;background:linear-gradient(180deg,#2a2522 0%,#3a302a 45%,#1e1a18 100%)}
.hero-shade{position:absolute;inset:0;background:radial-gradient(ellipse at 70% 40%,rgba(120,60,30,.35),transparent 60%)}
.brand{position:absolute;left:161px;top:30px;display:flex;align-items:center;gap:8px;color:var(--white);font-family:"Roboto Condensed",sans-serif;font-weight:700;font-size:18px;letter-spacing:1px}
.brand .mark{width:14px;height:14px;background:var(--orange)}
.nav{position:absolute;top:33px;font-size:11px;color:var(--white)}
.call{position:absolute;left:998px;top:21px;width:40px;height:40px;background:var(--orange);display:flex;align-items:center;justify-content:center}
.header-line{position:absolute;left:161px;top:82px;width:877px;height:1px;background:var(--line)}
.hero-tag{position:absolute;left:526px;top:204px;width:148px;height:35px;background:var(--white);color:var(--orange);font-family:"Roboto Condensed",sans-serif;font-weight:700;font-size:18px;display:flex;align-items:center;justify-content:center}
.hero-title{top:262px;font-size:56px;color:var(--white);letter-spacing:.5px}
.hero-text{top:338px;color:var(--white);font-size:12px;line-height:22px}

/* contact band */
.band{position:absolute;left:0;top:2336px;width:1200px;height:450px;background:linear-gradient(90deg,#1f1c1b 0%,#3b3029 50%,#231e1b 100%)}
.field{position:absolute;border:1px solid rgba(255,255,255,.55);background:rgba(255,255,255,.06);color:var(--white);font-size:10px;padding:10px 14px}
.upload{position:absolute;left:281px;top:2626px;width:636px;height:36px;border:1px dashed rgba(255,255,255,.55);background:rgba(255,255,255,.06);display:flex;align-items:center;gap:10px;padding:0 14px;color:var(--white);font-size:10px}
.upload-btn{margin-left:auto;border:1px solid var(--orange);color:var(--orange);padding:4px 12px;font-size:9px}

/* projects */
.project{position:absolute;top:3431px;width:166px;height:164px}
.circ-arrow{position:absolute;width:18px;height:18px}

/* testimonial */
.card{position:absolute;left:381px;top:3744px;width:527px;height:265px;background:var(--white);box-shadow:0 0 14px rgba(0,0,0,.12)}

/* footer */
.footer{position:absolute;left:0;top:4079px;width:1200px;height:422px;background:linear-gradient(180deg,#242120,#2f2926)}
.f-head{position:absolute;top:4240px;font-family:"Roboto Condensed",sans-serif;font-weight:700;font-size:15px;color:var(--orange)}
.f-text{position:absolute;font-size:10px;line-height:21px;color:var(--white)}
.f-links{position:absolute;top:4284px;font-size:10px;line-height:21px;color:var(--white);list-style:none}
.f-links li::before{content:"";display:inline-block;border-left:5px solid var(--orange);border-top:4px solid transparent;border-bottom:4px solid transparent;margin-right:9px}
.social{position:absolute;top:4453px;width:37px;height:37px;border:1px solid rgba(255,255,255,.6)}
</style>
</head>
<body>

<!-- HERO -->
<section class="hero" role="img" aria-label="Construction workers drilling on a building site">
  <div class="hero-shade"></div>
</section>
<div class="brand"><span class="mark"></span>BRIXMORVO</div>
<nav>
  <span class="nav" style="left:528px">Home</span>
  <span class="nav" style="left:587px">About Us</span>
  <span class="nav" style="left:666px">Services</span>
  <span class="nav" style="left:739px">Testimonials</span>
  <span class="nav" style="left:832px">Gallery</span>
  <span class="nav" style="left:896px">Contact Us</span>
</nav>
<div class="call"><svg width="20" height="20" viewBox="0 0 24 24"><path d="M6.6 10.8a15 15 0 0 0 6.6 6.6l2.2-2.2c.3-.3.7-.4 1-.2 1.1.4 2.3.6 3.6.6.6 0 1 .4 1 1V20c0 .6-.4 1-1 1A17 17 0 0 1 3 4c0-.6.4-1 1-1h3.5c.6 0 1 .4 1 1 0 1.3.2 2.5.6 3.6.1.3 0 .7-.2 1z" fill="#fff"/></svg></div>
<div class="header-line"></div>
<div class="hero-tag">BRIXMORVO</div>
<h1 class="abs heading center hero-title">THE HEIGHT, PORT</h1>
<p class="abs center hero-text">Lorem Ipsum is simply dummy text of the printing and typesetting industry. Lorem<br>Ipsum has been the industry's standard dummy text ever since the 1500s</p>
<div class="btn" style="left:507px;top:416px;width:187px;height:52px;font-size:20px">Get In Touch</div>
<div class="photo" style="left:961px;top:480px;width:75px;height:76px;background:linear-gradient(160deg,#8fa9c9,#2d3d55)" role="img" aria-label="Modern building thumbnail"></div>
<div class="dots" style="left:944px;top:466px;width:104px;height:13px"></div>
<div class="dots" style="left:1036px;top:479px;width:13px;height:90px"></div>
<svg class="abs" style="left:977px;top:580px" width="60" height="14" viewBox="0 0 60 14"><path d="M2 7h18M2 7l5-5M2 7l5 5M40 7h18M58 7l-5-5M58 7l-5 5" stroke="#fff" stroke-width="1.6" fill="none"/></svg>

<!-- WHAT WE PROVIDE -->
<h2 class="abs heading center" style="top:710px;font-size:32px">What We Provide?</h2>
<p class="abs center small" style="top:750px">Lorem Ipsum is simply dummy text of the printing and typesetting industry.<br>Lorem Ipsum has been the industry's standard dummy text.</p>

<!-- Scaffolding -->
<h3 class="abs heading" style="left:166px;top:900px;font-size:24px">Scaffolding</h3>
<p class="abs small" style="left:166px;top:956px;width:380px">Lorem Ipsum is simply dummy text of the printing and typesetting industry. Lorem Ipsum has been the industry's standard dummy text ever since the 1500s, when an unknown printer took a galley of type and scrambled it to make a type specimen book. It has survived not only five centuries, but also the leap into electronic typesetting, remaining essentially unchanged.</p>
<p class="abs small" style="left:166px;top:1075px;width:340px">It was popularised in the 1960s with the release of Letraset sheets containing Lorem Ipsum passages.</p>
<div class="btn" style="left:164px;top:1158px;width:98px;height:37px;font-size:13px">Read More</div>
<div class="dots" style="left:1053px;top:1100px;width:18px;height:193px"></div>
<div class="dots" style="left:975px;top:1280px;width:96px;height:14px"></div>
<div class="photo" style="left:767px;top:821px;width:278px;height:449px;background:linear-gradient(180deg,#8d9399,#6a6560 70%,#4a4541)" role="img" aria-label="Scaffolding tower beside an old building"></div>
<div class="photo" style="left:655px;top:887px;width:315px;height:315px;background:linear-gradient(180deg,#5f88c8 0%,#8aa7cf 40%,#b8a48a 75%,#6d5a48)" role="img" aria-label="Building wrapped in scaffolding"></div>

<!-- Elevation -->
<div class="dots" style="left:128px;top:1297px;width:96px;height:14px"></div>
<div class="dots" style="left:128px;top:1310px;width:14px;height:196px"></div>
<div class="photo" style="left:155px;top:1331px;width:278px;height:451px;background:linear-gradient(180deg,#8f8e93,#b08d7d 50%,#4c3f38)" role="img" aria-label="Curved concrete building facade"></div>
<div class="photo" style="left:231px;top:1398px;width:314px;height:314px;background:linear-gradient(170deg,#c7d4e4 0%,#9fb4cf 35%,#d09a5a 65%,#c59a8c)" role="img" aria-label="Wooden lattice architectural structure against the sky"></div>
<h3 class="abs heading" style="left:606px;top:1412px;font-size:24px">Elevation</h3>
<p class="abs small" style="left:606px;top:1468px;width:380px">Lorem Ipsum is simply dummy text of the printing and typesetting industry. Lorem Ipsum has been the industry's standard dummy text ever since the 1500s, when an unknown printer took a galley of type and scrambled it to make a type specimen book. It has survived not only five centuries, but also the leap into electronic typesetting, remaining essentially unchanged.</p>
<p class="abs small" style="left:606px;top:1584px;width:340px">It was popularised in the 1960s with the release of Letraset sheets containing Lorem Ipsum passages.</p>
<div class="btn" style="left:604px;top:1668px;width:98px;height:37px;font-size:13px">Read More</div>

<!-- Renovation -->
<h3 class="abs heading" style="left:166px;top:1868px;font-size:24px">Renovation</h3>
<p class="abs small" style="left:166px;top:1924px;width:380px">Lorem Ipsum is simply dummy text of the printing and typesetting industry. Lorem Ipsum has been the industry's standard dummy text ever since the 1500s, when an unknown printer took a galley of type and scrambled it to make a type specimen book. It has survived not only five centuries, but also the leap into electronic typesetting, remaining essentially unchanged.</p>
<p class="abs small" style="left:166px;top:2043px;width:340px">It was popularised in the 1960s with the release of Letraset sheets containing Lorem Ipsum passages.</p>
<div class="btn" style="left:164px;top:2126px;width:98px;height:37px;font-size:13px">Read More</div>
<div class="dots" style="left:1053px;top:2068px;width:18px;height:193px"></div>
<div class="dots" style="left:975px;top:2248px;width:96px;height:14px"></div>
<div class="photo" style="left:767px;top:1789px;width:278px;height:449px;background:linear-gradient(180deg,#d8d6d2,#b9b3aa 60%,#8e877e)" role="img" aria-label="Interior under renovation"></div>
<div class="photo" style="left:655px;top:1855px;width:315px;height:315px;background:linear-gradient(180deg,#c7a45a 0%,#e1cf9d 40%,#a9a39a 70%,#6c6257)" role="img" aria-label="Room with wooden window frames being renovated"></div>

<!-- CONTACT / QUOTE BAND -->
<section class="band" role="img" aria-label="Construction workers on site"></section>
<h2 class="abs heading center" style="top:2390px;font-size:32px;color:var(--white)">Looking For Something New?</h2>
<p class="abs center small" style="top:2441px;color:var(--white)">Lorem Ipsum is simply dummy text of the printing and typesetting industry.<br>Lorem Ipsum has been the industry's standard dummy text.</p>
<div class="field" style="left:281px;top:2514px;width:201px;height:38px">Name:</div>
<div class="field" style="left:498px;top:2514px;width:202px;height:38px">Phone:</div>
<div class="field" style="left:716px;top:2514px;width:201px;height:38px">Email:</div>
<div class="field" style="left:281px;top:2566px;width:636px;height:50px">Message:</div>
<div class="upload">
  <svg width="16" height="16" viewBox="0 0 16 16"><path d="M8 11V2M4.5 5.5L8 2l3.5 3.5M2 10v4h12v-4" stroke="#f28a1c" stroke-width="1.5" fill="none"/></svg>
  <span>Upload Photos:</span>
  <span class="upload-btn">Choose Files</span>
</div>
<div class="btn" style="left:540px;top:2678px;width:120px;height:37px;font-size:12px">Send A Message</div>

<!-- ABOUT -->
<div class="dots" style="left:133px;top:2836px;width:96px;height:14px"></div>
<div class="dots" style="left:133px;top:2849px;width:14px;height:196px"></div>
<div class="photo" style="left:236px;top:2935px;width:300px;height:300px;background:linear-gradient(180deg,#6f86b8 0%,#b8a2b6 55%,#e0b49c)" role="img" aria-label="Steel frame structure at dusk"></div>
<div class="photo" style="left:161px;top:2867px;width:277px;height:278px;background:linear-gradient(180deg,#e6e5e2,#bdb8ae 55%,#2e3145)" role="img" aria-label="Modern kitchen interior"></div>
<h2 class="abs heading" style="left:613px;top:2910px;font-size:32px">About Us</h2>
<p class="abs small" style="left:613px;top:2965px;width:380px">Lorem Ipsum is simply dummy text of the printing and typesetting industry. Lorem Ipsum has been the industry's standard dummy text ever since the 1500s, when an unknown printer took a galley of type and scrambled it to make a type specimen book. It has survived not only five centuries, but also the leap into electronic typesetting, remaining essentially unchanged.</p>
<p class="abs small" style="left:613px;top:3082px;width:340px">It was popularised in the 1960s with the release of Letraset sheets containing Lorem Ipsum passages.</p>
<div class="btn" style="left:611px;top:3169px;width:97px;height:37px;font-size:13px">Read More</div>

<!-- LATEST PROJECTS -->
<h2 class="abs heading center" style="top:3313px;font-size:32px">Latest Projects</h2>
<p class="abs center small" style="top:3353px">Lorem Ipsum is simply dummy text of the printing and typesetting industry.<br>Lorem Ipsum has been the industry's standard dummy text.</p>
<svg class="circ-arrow" style="left:106px;top:3516px" viewBox="0 0 18 18"><circle cx="9" cy="9" r="8" fill="none" stroke="#f28a1c" stroke-width="1.5"/><path d="M11 9H6M8 6.5L5.5 9 8 11.5" stroke="#f28a1c" stroke-width="1.5" fill="none"/></svg>
<div class="project" style="left:161px;background:linear-gradient(160deg,#3d5f86,#c8703a 60%,#8c8176)" role="img" aria-label="Worker on a construction site"></div>
<div class="project" style="left:339px;background:linear-gradient(180deg,#6f94c8,#c8c5c4 70%,#9f9690)" role="img" aria-label="Steel frame against a blue sky"></div>
<div class="project" style="left:517px;background:linear-gradient(180deg,#f0f2f5,#43618e 50%,#22304a)" role="img" aria-label="Modern glass building"></div>
<div class="project" style="left:695px;background:linear-gradient(180deg,#6f97d6,#2d3038 55%,#b8602a)" role="img" aria-label="Contemporary house exterior"></div>
<div class="project" style="left:873px;background:linear-gradient(180deg,#e8e8e6,#a9b09a 50%,#3a3d4e)" role="img" aria-label="Kitchen interior"></div>
<svg class="circ-arrow" style="left:1072px;top:3516px" viewBox="0 0 18 18"><circle cx="9" cy="9" r="8" fill="none" stroke="#f28a1c" stroke-width="1.5"/><path d="M7 9h5M10 6.5L12.5 9 10 11.5" stroke="#f28a1c" stroke-width="1.5" fill="none"/></svg>

<!-- TESTIMONIALS -->
<h2 class="abs heading center" style="top:3662px;font-size:32px;left:-6px">Our Testimonials</h2>
<div class="card"></div>
<div class="abs" style="left:320px;top:3809px;width:132px;height:136px;background:var(--white);box-shadow:0 0 12px rgba(0,0,0,.15)"></div>
<div class="photo" style="left:330px;top:3819px;width:112px;height:116px;background:linear-gradient(180deg,#e9e9ea,#8b8d92 55%,#1e2026)" role="img" aria-label="Client portrait"></div>
<svg class="circ-arrow" style="left:284px;top:3853px" viewBox="0 0 18 18"><circle cx="9" cy="9" r="8" fill="none" stroke="#f28a1c" stroke-width="1.5"/><path d="M9 12V6M6.5 8.5L9 6l2.5 2.5" stroke="#f28a1c" stroke-width="1.5" fill="none"/></svg>
<svg class="circ-arrow" style="left:284px;top:3883px" viewBox="0 0 18 18"><circle cx="9" cy="9" r="8" fill="none" stroke="#f28a1c" stroke-width="1.5"/><path d="M9 6v6M6.5 9.5L9 12l2.5-2.5" stroke="#f28a1c" stroke-width="1.5" fill="none"/></svg>
<div class="abs heading" style="left:473px;top:3783px;font-size:14px">Client Name</div>
<div class="abs" style="left:473px;top:3808px;font-size:9px">Elevation Worker</div>
<svg class="abs" style="left:473px;top:3824px" width="100" height="18" viewBox="0 0 100 18">
  <g fill="#f28a1c"><path id="s" d="M8 1l2 5.2 5.5.3-4.3 3.5 1.5 5.4L8 12.3 3.3 15.4l1.5-5.4L.5 6.5 6 6.2z"/><use href="#s" x="19"/><use href="#s" x="38"/><use href="#s" x="57"/></g>
  <use href="#s" x="76" fill="none" stroke="#f28a1c" stroke-width="1"/>
</svg>
<p class="abs" style="left:473px;top:3850px;width:412px;font-size:9.5px;line-height:21px">Lorem Ipsum is simply dummy text of the printing and typesetting industry. Lorem Ipsum has been the industry's standard dummy text ever since the 1500s, when an unknown printer took a galley of type and scrambled it to make a type specimen book.</p>
<p class="abs" style="left:473px;top:3934px;width:412px;font-size:9.5px;line-height:21px">It has survived not only five centuries, but also the leap into electronic typesetting, remaining essentially unchanged.</p>

<!-- FOOTER -->
<footer class="footer" role="img" aria-label="Dim construction site backdrop"></footer>
<div class="abs" style="left:0;width:1200px;top:4130px;display:flex;justify-content:center;align-items:center;gap:8px;color:var(--white);font-family:'Roboto Condensed',sans-serif;font-weight:700;font-size:22px;letter-spacing:1px"><span style="width:16px;height:16px;background:var(--orange)"></span>BRIXMORVO</div>
<div class="abs" style="left:161px;top:4202px;width:877px;height:1px;background:rgba(255,255,255,.2)"></div>

<div class="f-head" style="left:162px">Contact Info</div>
<p class="f-text" style="left:162px;top:4284px">100- Lorem Ipsum is simply<br>dummy text .</p>
<p class="f-text" style="left:162px;top:4345px"><span style="color:var(--orange)">Email:</span> info@brixmorvo.com</p>
<p class="f-text" style="left:162px;top:4389px"><span style="color:var(--orange)">Phone:</span> +91-000-000-000</p>

<div class="f-head" style="left:388px">Quick Links</div>
<ul class="f-links" style="left:388px"><li>Home</li><li>About Us</li><li>Services</li><li>Projects</li><li>Contact Us</li></ul>

<div class="f-head" style="left:613px">Useful Links</div>
<ul class="f-links" style="left:613px"><li>Company</li><li>Terms &amp; Conditions</li><li>Privacy Policy</li><li>Testimonials</li><li>Newsletter</li></ul>

<div class="f-head" style="left:838px">News Letter</div>
<div class="abs" style="left:837px;top:4292px;width:201px;height:39px;background:var(--white);font-size:10px;padding:12px 14px;color:#888">Email:</div>
<div class="btn" style="left:837px;top:4352px;width:143px;height:37px;font-size:15px">Subscribe Now</div>

<div class="abs" style="left:161px;top:4437px;width:877px;height:1px;background:rgba(255,255,255,.2)"></div>
<p class="f-text" style="left:162px;top:4462px">Copyright © 2020 Brixmorvo. All Rights Reserved.</p>
<div class="social" style="left:837px" aria-label="Social link"></div>
<div class="social" style="left:889px;background:var(--orange);border-color:var(--orange)" aria-label="Social link"></div>
<div class="social" style="left:942px" aria-label="Social link"></div>
<div class="social" style="left:994px" aria-label="Social link"></div>

</body>
</html>
```